Vintage label design for Electrical company (stickers)

I'm after a vintage label design for my electrical company, currently trying to break into the upper market in the electrical field so I need something that stands out and is easy to read.
These will be getting made into stickers roughly 90-110mm x 40-60mm with a custom rectangular shape.
The stickers should have

Target Market(s)

Upper electrical market

Industry/Entity Type

Electrical

Font styles to use
Serif
Decorative
Script

Colors
acd037
9ccb3b
33b8a4

Requirements
Must have
• Be unique, edgy, vintage/retro and easy to read. An electrical theme
• Company logo (picture provided below obviously a lime)
• Cobalt Wiring
• 0492815037
• Cobaltwiring.com
• Linkbook symbol
• as these are going to be stickers I would like my contact details on them
Nice to have
• Same shades of green, fit between 90-110mm x 40-60mm

```html
<!DOCTYPE html>
<html lang="en">
<head>
<meta charset="utf-8">
<title>Cobalt Wiring – Sticker Label</title>
<link href="https://fonts.googleapis.com/css2?family=Marcellus&family=Montserrat:wght@700&family=Pacifico&display=swap" rel="stylesheet">
<style>
  :root {
    --green-deep: #1d662c;
    --green-mid: #3c8f3e;
    --green-leaf: #9ccb3b;
    --green-lime: #acd037;
    --green-soft: #8fcf5a;
    --paper: #f3f3f2;
    --white: #ffffff;
  }
  html, body {
    margin: 0;
    padding: 0;
    width: 1200px;
    height: 837px;
    overflow: hidden;
    background: var(--paper);
  }
  .sticker {
    display: block;
    width: 1200px;
    height: 837px;
  }
  .band-title {
    font-family: "Marcellus", Georgia, serif;
    font-size: 34px;
    letter-spacing: 3px;
    fill: var(--white);
    opacity: 0.92;
  }
  .established {
    font-family: "Montserrat", Arial, sans-serif;
    font-size: 11px;
    letter-spacing: 1.5px;
    fill: var(--green-leaf);
  }
  .wordmark {
    font-family: "Pacifico", cursive;
    fill: var(--green-mid);
  }
  .social-name {
    font-family: "Montserrat", Arial, sans-serif;
    font-size: 10px;
    fill: var(--white);
  }
  .phone {
    font-family: "Montserrat", Arial, sans-serif;
    font-size: 24px;
    letter-spacing: 1px;
    fill: var(--white);
  }
  .website {
    font-family: "Montserrat", Arial, sans-serif;
    font-size: 11px;
    letter-spacing: 1px;
    fill: var(--white);
  }
  .licence {
    font-family: "Montserrat", Arial, sans-serif;
    font-size: 7px;
    letter-spacing: 1px;
    fill: var(--white);
  }
</style>
</head>
<body>
<svg class="sticker" viewBox="0 0 1200 837" xmlns="http://www.w3.org/2000/svg">
  <defs>
    <linearGradient id="rim-fill" x1="0" y1="0" x2="1" y2="1">
      <stop offset="0" stop-color="#2f8436"/>
      <stop offset="0.5" stop-color="#1d662c"/>
      <stop offset="1" stop-color="#2a7a33"/>
    </linearGradient>
    <linearGradient id="band-fill" x1="0" y1="0" x2="1" y2="0">
      <stop offset="0" stop-color="#1d662c"/>
      <stop offset="0.5" stop-color="#2c7d35"/>
      <stop offset="1" stop-color="#1d662c"/>
    </linearGradient>
    <clipPath id="inner-face">
      <circle cx="600" cy="418" r="222"/>
    </clipPath>
    <path id="title-arc" d="M425.2,354.4 A186,186 0 0 1 774.8,354.4"/>
  </defs>

  <!-- outer rim -->
  <circle cx="600" cy="418" r="250" fill="url(#rim-fill)"/>
  <circle cx="600" cy="418" r="242" fill="none" stroke="var(--white)" stroke-width="1" stroke-dasharray="3 3" opacity="0.8"/>
  <circle cx="600" cy="418" r="226" fill="none" stroke="var(--green-soft)" stroke-width="6"/>
  <circle cx="600" cy="418" r="222" fill="var(--white)"/>

  <g clip-path="url(#inner-face)">
    <!-- top name band -->
    <path d="M398.9,324.1 A222,222 0 0 1 801.1,324.1 L755.8,345.3 A172,172 0 0 0 444.2,345.3 Z" fill="url(#band-fill)"/>
    <!-- contact band -->
    <rect x="370" y="500" width="460" height="150" fill="url(#band-fill)"/>
  </g>

  <text class="band-title" text-anchor="middle">
    <textPath href="#title-arc" startOffset="50%">COBALT WIRING</textPath>
  </text>

  <!-- brand lockup -->
  <circle cx="600" cy="318" r="34" fill="var(--green-lime)"/>
  <text class="established" x="612" y="376" text-anchor="middle">EST. 2015</text>
  <text class="wordmark" x="600" y="432" font-size="66" text-anchor="middle">Cobalt</text>
  <text class="wordmark" x="612" y="480" font-size="40" text-anchor="middle">Wiring</text>

  <!-- contact details -->
  <circle cx="570" cy="530" r="6" fill="var(--green-soft)"/>
  <text class="social-name" x="581" y="534">Linkbook</text>
  <text class="phone" x="600" y="562" text-anchor="middle">0492815037</text>
  <text class="website" x="600" y="580" text-anchor="middle">COBALTWIRING.COM</text>
  <text class="licence" x="600" y="596" text-anchor="middle">R.E.C 30472</text>
</svg>
</body>
</html>
```